Design Card that Captures Life's Moments

Thinking black and white design with maybe some accent colors. Open to others too. Looking for bold and modern to accompany new logo design. For the side without my info, would have tagline of "Capturing Life's Moments" with either logo or website tessabrimphotography.com. I want the tagline to dominate and be the main focus of that side.

Target Market(s)

Something that can appeal to people who might be interested in family/kids, business, sports, commercial, or birth/newborn photography.

Industry/Entity Type

Professional Photography

Contact Information for Business Card

Font styles to use
Sans Serif
Script
Other font styles liked:
• Go with Logo, but the tagline could be script that popped.

Requirements
Must have
• See details above! Wow factor! Make someone pick my card up and take it home or at least to look at it further.
• Tagline: Capturing Life's Moments (Main text on side without name)
• INFO:
• Tessa Brimford-Kole - Photographer
• 555-213-0476 - Cell and for SMS
• www.tessabrimphotography.com - Website (maybe on side with tagline?)
• tessa@tessaphotographs.com - Email
Nice to have
• JUST AN IDEA... I would like to see Capturing Life's Moment really take over most of one side of the card. Think greeting card. Where you can't miss it. It is in your face, but nice and elegant. Maybe cursive, but could work with other font. Instead of logo on tagline side, just have tessabrimphotography.com in smaller text along one of the edges.
Should not have
• Too simple I could of created it, like with only my logo and some typed text.

```html
<!DOCTYPE html>
<html lang="en">
<head>
<meta charset="utf-8">
<title>Tessa Brim Photography – Business Card</title>
<link rel="stylesheet" href="https://fonts.googleapis.com/css2?family=Great+Vibes&family=Montserrat:wght@400;500;600;700&display=swap">
<style>
  :root {
    --backdrop: #7b6e6f;
    --card-dark: #2b2725;
    --card-light: #ffffff;
    --ink: #1c1a1a;
    --paper-line: #f4f1ee;
    --accent-teal: #2b92a8;
    --muted-grey: #6d6a6a;
    --shadow: rgba(30, 20, 22, 0.35);
  }

  * { margin: 0; padding: 0; box-sizing: border-box; }

  html, body {
    width: 1200px;
    height: 1000px;
    overflow: hidden;
    background: var(--backdrop);
  }

  .canvas {
    position: relative;
    width: 1200px;
    height: 1000px;
    display: flex;
    flex-direction: column;
    align-items: center;
    justify-content: center;
    gap: 60px;
  }

  .card {
    position: relative;
    width: 700px;
    height: 400px;
    box-shadow: 0 14px 30px var(--shadow);
    display: flex;
    flex-direction: column;
    align-items: center;
    justify-content: center;
  }

  /* double frame: thick outer rule + thin inner rule */
  .card__frame {
    position: absolute;
    inset: 24px;
    border: 5px solid;
    pointer-events: none;
  }
  .card__frame::after {
    content: "";
    position: absolute;
    inset: 5px;
    border: 1.5px solid;
  }

  /* tagline side */
  .card--tagline { background: var(--card-dark); }
  .card--tagline .card__frame,
  .card--tagline .card__frame::after { border-color: var(--paper-line); }

  .tagline {
    font-family: "Great Vibes", cursive;
    font-size: 72px;
    color: var(--paper-line);
    line-height: 1;
    margin-top: 10px;
  }

  .website {
    position: absolute;
    bottom: 62px;
    font-family: "Montserrat", sans-serif;
    font-weight: 600;
    font-size: 15px;
    letter-spacing: 3px;
    color: var(--accent-teal);
  }

  /* contact side */
  .card--contact { background: var(--card-light); }
  .card--contact .card__frame,
  .card--contact .card__frame::after { border-color: var(--ink); }

  .brand {
    display: flex;
    align-items: center;
    gap: 10px;
    font-family: "Montserrat", sans-serif;
    font-weight: 500;
    font-size: 26px;
    color: var(--ink);
    letter-spacing: 1px;
    margin-bottom: 24px;
  }
  .brand__dot {
    width: 10px;
    height: 10px;
    border-radius: 50%;
    background: var(--ink);
  }

  .contact-name {
    font-family: "Montserrat", sans-serif;
    font-weight: 600;
    font-size: 17px;
    letter-spacing: 3px;
    text-transform: uppercase;
    color: var(--accent-teal);
  }
  .contact-role {
    font-family: "Montserrat", sans-serif;
    font-weight: 500;
    font-size: 14px;
    letter-spacing: 4px;
    text-transform: uppercase;
    color: var(--muted-grey);
    margin-top: 6px;
  }
  .contact-phone {
    font-family: "Montserrat", sans-serif;
    font-weight: 700;
    font-size: 17px;
    letter-spacing: 3px;
    color: var(--ink);
    margin-top: 8px;
  }
  .contact-email {
    font-family: "Montserrat", sans-serif;
    font-weight: 500;
    font-size: 15px;
    letter-spacing: 2px;
    color: var(--muted-grey);
    margin-top: 6px;
  }
</style>
</head>
<body>
  <main class="canvas">
    <section class="card card--tagline">
      <div class="card__frame"></div>
      <p class="tagline">Capturing Life's Moments</p>
      <p class="website">www.tessabrimphotography.com</p>
    </section>

    <section class="card card--contact">
      <div class="card__frame"></div>
      <div class="brand">
        <span class="brand__dot"></span>
        <span class="brand__name">Tessa Brim Photography</span>
      </div>
      <p class="contact-name">Tessa Brimford-Kole</p>
      <p class="contact-role">Photographer</p>
      <p class="contact-phone">555 213 0476</p>
      <p class="contact-email">tessa@tessaphotographs.com</p>
    </section>
  </main>
</body>
</html>
```